Business Card Design Project

I would like to redesign our business cards and change the look and feel of our marketing material, but maintain the same basic identity of our current logo.
It is my belief that it could be much better.
You can view our website at kducn.com

   

I was looking for a completely different look.  Something much more hip and cool looking.  You can change the colors.

I like this look and feel

 http://www.hudlawfirm.com

 But obviously don’t want to copy them exactly.

 

For the back just leave the last point.

“Focus on Your Business, and We’ll Focus on Your Claim”

I want there to be space for someone to write on.

                                                                    

                                       

I like this look and feel

 http://www.hudlawfirm.com

```html
<!DOCTYPE html>
<html lang="en">
<head>
<meta charset="utf-8">
<title>Business Card – Back</title>
<link rel="stylesheet" href="https://fonts.googleapis.com/css2?family=Fira+Sans+Condensed:ital,wght@1,400&display=swap">
<style>
  :root {
    --stage-bg: #bfbfbf;
    --card-bg: #ffffff;
    --ink: #2b2b2b;
    --brand-blue: #00529b;
    --art-light: #ededed;
    --art-dark: #d9d9d9;
  }
  * { margin: 0; padding: 0; box-sizing: border-box; }
  html, body {
    width: 1200px;
    height: 1000px;
    overflow: hidden;
    background: var(--stage-bg);
  }
  .card-back {
    position: absolute;
    left: 75px;
    top: 200px;
    width: 1050px;
    height: 600px;
    background: var(--card-bg);
    overflow: hidden;
  }
  .swing-art {
    position: absolute;
    left: 8px;
    top: 0;
    width: 222px;
    height: 205px;
    background: linear-gradient(160deg, var(--art-light), var(--art-dark));
  }
  .tagline {
    position: absolute;
    left: 230px;
    top: 150px;
    font-family: "Fira Sans Condensed", "Arial Narrow", sans-serif;
    font-style: italic;
    font-weight: 400;
    font-size: 29px;
    letter-spacing: -0.3px;
    color: var(--ink);
    white-space: nowrap;
    transform: rotate(-2deg);
    transform-origin: left center;
  }
  .wave-band {
    position: absolute;
    left: 0;
    top: 0;
    width: 1050px;
    height: 600px;
  }
  .wave-band path { fill: var(--brand-blue); }
</style>
</head>
<body>
  <section class="card-back">
    <div class="swing-art" role="img" aria-label="Hand-drawn sketch of an empty hanging swing seat in grey ink"></div>
    <p class="tagline">“Focus on Your Business, and We’ll Focus on Your Claim”</p>
    <svg class="wave-band" viewBox="0 0 1050 600" aria-hidden="true">
      <path d="M0 462 C 250 464, 500 525, 700 523 C 850 522, 970 495, 1050 462 L1050 600 L0 600 Z"/>
    </svg>
  </section>
</body>
</html>
```